General Dental Office Business Card

I run a private general dental office in southern California, and would like a refresh/redesign of my business card. I focus on quality care rather than volume. The email address on the uploaded current card should be updated to: info@maplecovedental.example. The current card's logo is a deboss, but I am open to other ideas. The logo can be refreshed, but it is something that's been with me since the beginning of the office, so I wouldn't want a drastic redesign.
Target Market(s)
Adults 18-99, whoever needs dental services
Industry/Entity Type
Healthcare/Dental
Contact Information for Business Card
Name, Address, Phone, email
Colors
Designer to choose colors to be used in the design.
Requirements
Must have
- Logo (Same as original one in the uploaded file), space on back for appointment time/date

```html
<!DOCTYPE html>
<html lang="en">
<head>
<meta charset="utf-8">
<title>Maple Cove Dental — Business Card</title>
<link rel="stylesheet" href="https://fonts.googleapis.com/css2?family=PT+Sans:wght@400;700&display=swap">
<style>
  :root {
    --teal: #1fb2c4;
    --teal-deep: #10a3b4;
    --teal-bright: #27d4ee;
    --ink: #222222;
    --rule-grey: #a9a9a9;
    --paper: #ffffff;
    --backdrop: #2b2b2b;
  }
  * { box-sizing: border-box; margin: 0; padding: 0; }
  html, body {
    width: 1200px; height: 1108px; overflow: hidden;
    background: var(--backdrop);
    font-family: "PT Sans", "Helvetica Neue", Arial, sans-serif;
  }
  .card-set {
    position: absolute; inset: 0;
    display: flex; justify-content: center; align-items: center; gap: 60px;
  }
  .card {
    width: 420px; height: 720px; border-radius: 26px; overflow: hidden;
    box-shadow: 0 20px 40px rgba(0,0,0,.45);
  }
  .card-front {
    background: var(--paper);
    padding: 64px 44px 40px;
    display: flex; flex-direction: column; align-items: center; text-align: center;
    color: var(--ink);
  }
  .brand {
    display: flex; align-items: center; gap: 18px; align-self: flex-start;
    margin-bottom: 50px;
  }
  .brand-dot {
    width: 70px; height: 70px; border-radius: 50%;
    border: 4px solid var(--teal); flex: none;
  }
  .brand-name {
    color: var(--teal); font-weight: 400; font-size: 34px; line-height: 1.05;
    text-transform: uppercase; text-align: left; letter-spacing: .5px;
  }
  .doctor-name {
    color: var(--teal); font-size: 30px; font-weight: 400; text-transform: uppercase;
    letter-spacing: .3px;
  }
  .doctor-title { font-size: 20px; margin-top: 2px; }
  .divider {
    width: 60px; height: 2px; background: var(--teal); margin: 16px auto;
  }
  .contact-line { font-size: 18px; line-height: 1.35; }
  .contact-line .accent { color: var(--teal); }
  .appointment-heading {
    color: var(--teal); font-size: 27px; margin: 4px 0 18px;
  }
  .appointment-fields { width: 100%; text-align: left; font-size: 16px; color: #555; }
  .field {
    display: flex; justify-content: space-between; align-items: flex-end;
    border-bottom: 1px solid var(--rule-grey); padding-bottom: 4px; margin-bottom: 26px;
  }
  .field span:only-child { flex: 1; }
  .card-back {
    background: radial-gradient(circle at 80% 20%, var(--teal-bright) 0%, var(--teal) 45%, var(--teal-deep) 100%);
  }
</style>
</head>
<body>
  <main class="card-set">
    <section class="card card-front" aria-label="Card front">
      <header class="brand">
        <span class="brand-dot"></span>
        <span class="brand-name">Maple Cove<br>Dental</span>
      </header>

      <h1 class="doctor-name">Daniel R. Hale DDS</h1>
      <p class="doctor-title">General Dentistry</p>

      <span class="divider"></span>

      <p class="contact-line">949-555-0147</p>
      <p class="contact-line">info@maplecovedental.example</p>
      <p class="contact-line">www.<span class="accent">maplecovedental</span>.example</p>

      <span class="divider"></span>

      <p class="contact-line">2185 Harbor View Road</p>
      <p class="contact-line">Seacliff, CA 92699</p>

      <span class="divider"></span>

      <h2 class="appointment-heading">Your Next Appointment</h2>
      <div class="appointment-fields">
        <div class="field"><span>Name</span></div>
        <div class="field"><span>Date</span><span>Time</span><span>am/pm</span></div>
      </div>
    </section>

    <section class="card card-back" role="img" aria-label="Card back: teal field with a repeating debossed pattern of the practice emblem"></section>
  </main>
</body>
</html>
```